Thorvane Leadership Flyer - Redesign

Thorvane Consulting is looking to update and redesign our one page leave behind. This page is part of the package left with prospective clients after meetings. It explains what Thorvane does. Recently, we used pixel forum to create a new logo for our new business name "Thorvane Leadership". We would like this new logo to replace the current "Thorvane Consulting" logo. We are looking for this re-designed piece to be easy to read, clean and professional, updating the design, including the graphics and layout. We typically use shades of blue (as in the Thorvane Leaderhip logo - attached).

Target Market(s)

Prospective clients

Industry/Entity Type

Management Consulting

Font styles to use
Serif
Sans Serif

Colors
3176b5
33a6d7
85cae6
0255a3
3276b5
85abd2
cfdeed
cee9f5

Requirements
Must have
• New Thorvane Leadership logo in place of the Thorvane Consulting logo.
• Professional design.
• Formatted so that simple copy changes can be easily made, as necessary.
Should not have
• More than one page

```html
<!DOCTYPE html>
<html lang="en">
<head>
<meta charset="utf-8">
<title>Thorvane Leadership – Flyer</title>
<link rel="stylesheet" href="https://fonts.googleapis.com/css2?family=Arimo:ital,wght@0,400;0,700;1,400;1,700&display=swap">
<style>
  :root {
    --blue-main: #3176b5;
    --blue-bright: #33a6d7;
    --blue-sky: #85cae6;
    --blue-deep: #0255a3;
    --blue-soft: #85abd2;
    --blue-pale: #cfdeed;
    --sidebar-bg: #d6ebf6;
    --ink: #2a2a2a;
    --ink-soft: #3c3c3c;
    --page: #fdfdfb;
    --backdrop: #e9e8e6;
  }
  * { box-sizing: border-box; margin: 0; padding: 0; }
  html, body {
    width: 1200px; height: 1200px; overflow: hidden;
    background: var(--backdrop);
    font-family: "Arimo", Arial, sans-serif;
    color: var(--ink);
  }
  .flyer {
    position: absolute; left: 160px; top: 30px;
    width: 880px; height: 1140px;
    background: var(--page);
    display: flex;
    box-shadow: 0 2px 10px rgba(0,0,0,.12);
  }
  .main { width: 610px; padding: 58px 34px 40px 56px; }
  .sidebar {
    width: 270px; background: var(--sidebar-bg);
    padding: 56px 22px 30px 26px;
    display: flex; flex-direction: column;
    font-size: 12.6px; line-height: 1.5; color: var(--ink-soft);
  }
  .brand { display: flex; align-items: center; gap: 12px; }
  .brand-dot { width: 46px; height: 46px; border-radius: 50%; background: var(--blue-main); }
  .brand-name { font-size: 34px; font-weight: 700; color: var(--blue-deep); letter-spacing: .5px; }
  .tagline-rule { border: 0; border-top: 1.5px solid var(--blue-soft); margin: 26px 0 4px; }
  .tagline {
    text-align: right; font-size: 30px; font-style: italic; font-weight: 700;
    color: var(--blue-main); letter-spacing: .5px; margin-bottom: 22px;
  }
  .main h2 {
    font-size: 15px; font-weight: 400; color: var(--blue-main);
    margin: 18px 0 2px;
  }
  .main p { font-size: 13.6px; line-height: 1.42; text-align: justify; }
  .main p + p { margin-top: 0; }
  .main p.indent { text-indent: 18px; }
  .main p.gap { margin-top: 18px; }
  .lead-term { color: var(--blue-main); font-size: 14.5px; }
  .sidebar h3 { font-size: 14px; font-weight: 400; color: var(--blue-main); margin: 16px 0 3px; }
  .sidebar h3:first-child { margin-top: 0; }
  .sidebar p { text-align: justify; }
  .sidebar .item { text-indent: 14px; }
  .sidebar .contact { margin-top: auto; }
  .contact h3 { font-size: 14.5px; margin-bottom: 10px; }
  .contact-grid {
    display: grid; grid-template-columns: 1fr auto; column-gap: 8px;
    font-size: 10.5px; line-height: 1.75;
  }
  .contact-grid span:nth-child(even) { text-align: right; }
</style>
</head>
<body>
<article class="flyer">
  <section class="main">
    <header>
      <div class="brand">
        <span class="brand-dot"></span>
        <span class="brand-name">Thorvane Leadership</span>
      </div>
      <hr class="tagline-rule">
      <p class="tagline">We Grow Leaders</p>
    </header>

    <h2>Why Choose Thorvane Consulting?</h2>
    <p class="indent">Companies and organizations that are serious and committed to the development of leaders and leadership skills seek out Thorvane Consulting. Here's why they choose us:</p>
    <p class="indent"><span class="lead-term">Expertise.</span> We're experts in an area where guessing can result in failure.</p>
    <p><span class="lead-term">Availability.</span> We're never off duty when it comes to meeting our clients' needs.</p>
    <p class="indent">Each client's needs are unique and we approach them that way. In our business, we know that while solutions may be similar, they are never identical.</p>
    <p class="indent">Our clients are our credentials. We are wholly and completely committed to our clients and see our relationship with them as of paramount importance.</p>
    <p class="indent">We're systematic. Leadership is a process, a collection of related activities, the purpose of which is to get the job done. We never lose sight of this primary purpose.</p>

    <h2>Capabilities</h2>
    <p class="indent">Thorvane Consulting has a broad bandwidth capability, able to apply leadership and organizational development professionals possessing a multitude of disciplines in fulfillment of its contractual requirements. In this vein, we are able to deploy facilitators, instructors and trainers and leader developers across the breadth of large organizations simultaneously. We are able to deploy certified leadership coaches on a broad scale, able to meet the needs of clients with significant and multiple simultaneous coaching requirements.</p>
    <p class="indent gap">In addition, we are certified to administer and interpret numerous diagnostic and developmental instruments including the Harlow Preference Type Indicator, Kessel EQi, RIVO B, the Calder Psychological Indicator (CPI), and many other vital measures for leader development.</p>
    <p class="indent gap">Daniel Thorvane, Principal, Thorvane Consulting, leads a team of skilled and committed professionals who are wholly dedicated to meeting the needs of their clients. Daniel has been developing leaders in organizations for nearly three decades. He is a retired Army officer, having focused on developing leaders while a Tactical Officer (Leader Developer) at the National Military Academy and throughout his military and civilian careers. He holds a Master of Arts in Leadership Development from the National Military Academy, Ridgefield, and a B.S. in Management from the University of Eastbrook.</p>
    <p class="indent gap">Thorvane Consulting has worked with thousands of governmental and corporate leaders since its inception in 2001. The firm is one of the very few in the field of leadership development that possesses an in-depth understanding of the scientific and research-based approaches to leadership development coupled with the experience of consultants and leader developers who have led small, large, and highly complex organizations and multi-disciplined matrix organizations.</p>
  </section>

  <aside class="sidebar">
    <h3>Our Programs and Offerings</h3>
    <p class="item">All of our programs are designed, from start to completion, to meet the specific needs of our clients. We believe this approach is unique and invaluable to our clients. With that in mind, some of our previous solutions for our clients have included:</p>

    <h3>Leadership Training Programs</h3>
    <p class="item"><em>Taking Charge</em> (new supervisor training programs)</p>
    <p class="item"><em>From Day One</em> (leading and integrating new team members)</p>
    <p class="item"><em>Manager as Leader, Leader as Coach</em> (motivation at its best)</p>
    <p class="item"><em>Leading the Team</em> (strategies, techniques, and tactics for leading groups)</p>

    <h3>Leadership Development</h3>
    <p class="item"><strong><em>Knowing the Leader</em></strong> (Oneself) Testing, interpretation, analysis, individual development planning</p>
    <p class="item"><strong><em>The Leading Edge Program</em></strong> (comprehensive, holistic, approach to leader development)</p>
    <p class="item"><strong><em>Listening for Leaders</em></strong> (the most important skill a leader can master)</p>

    <h3>Executive and Leadership Coaching</h3>
    <p class="item"><strong><em>Coaching for Performance</em></strong> (focusing on breakthrough performance and increased responsibilities)</p>
    <p class="item"><strong><em>Coaching for Strength</em></strong> (focusing on reassessment and realignment with a goal of measured improvement)</p>

    <h3>Performance Consulting</h3>
    <p class="item">Performance management systems based on client need</p>
    <p class="item">Change leadership and management strategies</p>

    <div class="contact">
      <h3>For more information contact :</h3>
      <div class="contact-grid">
        <span>Thorvane Consulting, LLC at</span><span>1-555-014-2288</span>
        <span>www.thorvaneconsulting.example</span><span>DUNS: 071593864</span>
        <span>1470 Larkspur Ave., Ste. 2B</span><span>VA Verified SDVOB</span>
        <span>Riverton, LA 70999</span><span>Thorvane Consulting, LLC</span>
      </div>
    </div>
  </aside>
</article>
</body>
</html>
```